Software development and consultancy website

Company – Velmoria Limited , London, UK
Profile – we are providing integration solutions development / consultancy services for QOR integration projects across UK.
Our name refers two words - integration and grace - and it shows our clients our main specialization field and key characteristics of our solutions / products. We also would like to be associated with follow words: smart, reliable, unique.
The target audience is experienced IT professionals and managers.
Website look and feel should be professional and sophisticated, simple and elegant. I like minimalistic themes with no real object/people photos. Try to avoid messy/cluttered/colourful content. White dominating background is a must, don’t like dark websites.
I would prefer light, web 2.0 style colours, follow are in my main interest:
- combination of light grey and orange
- Logo colours
In terms of deliverables, theme should be coded and be ready to be placed to my test website. I would also suggest if you could create skin for Tundle theme. NOTE: Please make a quote excluding Tundle theme cost.
Attached are examples of logo and corporate stationery design and mockups of website with landing page layout and content page layout. Website design should not copy stationery design but to be consistent with.
Sites I like :
http://www.brelwickpost.com/
http://www.vantrel.com/
http://www.holmfarq.com/quillscope/
http://www.dorvique.com/
I changed project type to Context and increased the budget. Please refer project description for details
It Company

```html
<!DOCTYPE html>
<html lang="en">
<head>
<meta charset="utf-8">
<title>Velmoria – Smart Solutions for QOR Process Integration</title>
<link rel="stylesheet" href="https://fonts.googleapis.com/css2?family=Source+Sans+3:wght@400;600;700&family=Arimo:wght@400;700&display=swap">
<style>
:root{
  --white:#ffffff;
  --ink:#333333;
  --muted:#666666;
  --navy:#1f3d7a;
  --sky:#3aa7dc;
  --hero-top:#3ba2d8;
  --hero-bottom:#1b2e68;
  --orange:#e8870f;
  --orange-dark:#c96f05;
  --green:#7fae1c;
  --green-dark:#5f8c0e;
  --blue-btn:#2a9bd6;
  --panel-line:#bdbdbd;
  --link:#1c9ad6;
  --foot-top:#3b3b3b;
  --foot-bottom:#141414;
  --soft:#efefef;
}
*{box-sizing:border-box;margin:0;padding:0}
html,body{width:972px;height:1200px;overflow:hidden;background:var(--white)}
body{font-family:"Source Sans 3",Calibri,sans-serif;color:var(--ink)}
.page{position:absolute;left:0;top:0;width:960px;height:1185px;transform:scale(1.0125);transform-origin:0 0}
.abs{position:absolute}

/* header */
.brand{left:67px;top:18px;display:flex;align-items:center;gap:9px}
.brand-dot{width:36px;height:36px;border-radius:50%;background:var(--orange)}
.brand-name{font-size:38px;font-weight:700;color:#555;letter-spacing:.5px;line-height:1}
.nav a{position:absolute;top:37px;font-family:Arimo,Arial,sans-serif;font-size:11px;color:#444;text-decoration:none}
.nav .active{left:745px;top:32px;width:66px;height:20px;background:var(--green);color:var(--white);padding:5px 0 0 6px}
.dropdown{left:745px;top:50px;width:97px;background:var(--green);border:1px solid var(--green-dark)}
.dropdown a{display:block;height:19px;padding:4px 0 0 5px;font-family:Arimo,Arial,sans-serif;font-size:9px;color:var(--white);text-decoration:none;border-bottom:1px solid #a7cf4e}

/* hero */
.hero{left:0;top:88px;width:960px;height:342px;background:linear-gradient(var(--hero-top),#2b73b0 55%,var(--hero-bottom))}
.hero-edge{left:0;top:428px;width:960px;height:9px;background:#1a2c5e}
.hero-shade{left:0;top:437px;width:960px;height:24px;background:linear-gradient(#e3e3e3,var(--white))}
.hero-title{left:70px;top:100px;font-size:19px;color:var(--white)}
.feature-card{left:59px;top:134px;width:455px;height:281px;background:var(--white);border-radius:8px}
.feature-heading{left:76px;top:160px;font-size:16px;color:var(--navy);width:123px;border-bottom:1px solid var(--navy);padding-bottom:2px}
.feature-list{left:68px;top:199px;list-style:none;font-size:11px;line-height:15px;color:var(--ink)}
.feature-list li{position:relative;padding-left:20px;margin-bottom:11px;width:145px}
.feature-list svg{position:absolute;left:0;top:3px}
.product-shot{left:222px;top:143px;width:275px;height:229px;background:linear-gradient(#d9dee4,#f2f3f5 40%,#e6e9ec);border:1px solid #aab}
.info-badge{left:209px;top:347px}
.download{left:275px;top:377px;width:173px;height:33px;border-radius:17px;background:linear-gradient(#8fd0f2,#2c86c6);border:2px solid #1f5f9b;color:var(--white);font-weight:700;font-size:17px;text-align:center;line-height:29px;letter-spacing:.3px}
.slide-arrow{top:241px}
.pitch-title{left:567px;top:126px;width:343px;height:44px;background:var(--sky);color:var(--white);font-size:19px;text-align:center;line-height:44px}
.pitch-btn{left:596px;width:123px;height:32px;border-radius:3px;color:var(--white);font-size:14px;text-align:center;line-height:31px}
.pitch-text{font-size:11px;line-height:17px;color:var(--white);width:205px}
.btn-orange{background:linear-gradient(#f39a2a,var(--orange-dark))}
.btn-green{background:linear-gradient(#8fc02a,var(--green-dark))}
.btn-blue{background:linear-gradient(#3fb0e6,#1f86c3)}

/* panels */
.panel{background:var(--white);border:1px solid var(--panel-line)}
.panel-head{height:32px;color:var(--white);font-size:18px;line-height:32px;padding-left:22px;border-radius:3px}
.head-green{background:linear-gradient(#8fc02a,var(--green-dark))}
.head-orange{background:linear-gradient(#f39a2a,var(--orange-dark))}
.head-blue{background:linear-gradient(#3fb0e6,#1f86c3)}
.head-grey{background:linear-gradient(#777,#3e3e3e)}
.copy{font-size:11px;line-height:17px;color:var(--ink)}
.photo{background:linear-gradient(135deg,#e9e9e9,#c9c9c9)}
.form-label{font-size:10px;color:var(--ink)}
.field{background:var(--white);border:1px solid #aaa;border-radius:4px}
.submit-orange{left:692px;top:698px;width:63px;height:23px;border-radius:3px;background:linear-gradient(#f39a2a,var(--orange-dark));color:var(--white);font-size:10px;text-align:center;line-height:23px}
.thumb{width:61px;height:61px;border:1px solid #ddd}
.date{font-size:11px;color:var(--ink)}
.more{font-size:10px;color:var(--link)}
.newsletter{left:590px;top:939px;width:274px;height:108px;background:var(--soft)}
.newsletter-title{left:616px;top:953px;font-size:14px;color:var(--ink)}
.submit-dark{left:637px;top:1011px;width:77px;height:23px;border-radius:7px;background:linear-gradient(#7a8a90,#2d3a40);border:1px solid #111;color:var(--white);font-size:11px;text-align:center;line-height:21px}

/* footer */
.footer{left:0;top:1090px;width:960px;height:95px;background:linear-gradient(var(--foot-top),var(--foot-bottom))}
.foot-text{font-family:Arimo,Arial,sans-serif;font-size:10px;line-height:15px;color:var(--white)}
.social{width:26px;height:26px;border-radius:3px;background:#3d77b8;top:1107px}
.feed{left:851px;top:1145px;width:26px;height:26px;border-radius:50%;background:var(--orange)}
</style>
</head>
<body>
<div class="page">

  <header>
    <div class="abs brand"><span class="brand-dot"></span><span class="brand-name">Velmoria</span></div>
    <nav class="nav">
      <a style="left:620px">HOME</a>
      <a style="left:675px">ABOUT US</a>
      <a class="active">PRODUCTS</a>
      <a style="left:828px">SERVICES</a>
      <a style="left:901px">BLOG</a>
    </nav>
    <div class="abs dropdown"><a>PRODUCT 1</a><a>PRODUCT 2</a><a style="border-bottom:0">PRODUCT 3</a></div>
  </header>

  <section>
    <div class="abs hero"></div>
    <div class="abs hero-edge"></div>
    <div class="abs hero-shade"></div>
    <h1 class="abs hero-title" style="font-weight:400">Smart Solutions for your QOR Process Integration projects</h1>

    <svg class="abs slide-arrow" style="left:10px" width="28" height="28" viewBox="0 0 28 28"><circle cx="14" cy="14" r="14" fill="#3aa7dc"/><path d="M16 8l-6 6 6 6" stroke="#fff" stroke-width="3" fill="none"/></svg>
    <svg class="abs slide-arrow" style="left:530px" width="28" height="28" viewBox="0 0 28 28"><circle cx="14" cy="14" r="14" fill="#3aa7dc"/><path d="M12 8l6 6-6 6" stroke="#fff" stroke-width="3" fill="none"/></svg>

    <div class="abs feature-card"></div>
    <h2 class="abs feature-heading" style="font-weight:400">Featured Product</h2>
    <ul class="abs feature-list">
      <li><svg width="13" height="13" viewBox="0 0 13 13"><circle cx="6.5" cy="6.5" r="6.5" fill="#555"/><path d="M5 4l3 2.5L5 9" stroke="#fff" stroke-width="1.5" fill="none"/></svg>Lorem ipsum dolor sit am et, consectetuer elit.</li>
      <li><svg width="13" height="13" viewBox="0 0 13 13"><circle cx="6.5" cy="6.5" r="6.5" fill="#555"/><path d="M5 4l3 2.5L5 9" stroke="#fff" stroke-width="1.5" fill="none"/></svg>Lorem ipsum dolor sit am et, consectetuer elit.</li>
      <li><svg width="13" height="13" viewBox="0 0 13 13"><circle cx="6.5" cy="6.5" r="6.5" fill="#555"/><path d="M5 4l3 2.5L5 9" stroke="#fff" stroke-width="1.5" fill="none"/></svg>Lorem ipsum dolor sit am et, consectetuer elit.</li>
      <li><svg width="13" height="13" viewBox="0 0 13 13"><circle cx="6.5" cy="6.5" r="6.5" fill="#555"/><path d="M5 4l3 2.5L5 9" stroke="#fff" stroke-width="1.5" fill="none"/></svg>Lorem ipsum dolor sit am et, consectetuer elit.</li>
    </ul>
    <div class="abs product-shot" role="img" aria-label="Screenshot of the featured website template product"></div>
    <svg class="abs info-badge" width="28" height="28" viewBox="0 0 28 28"><circle cx="14" cy="14" r="13" fill="#f0a020" stroke="#c87400"/><circle cx="14" cy="8" r="2" fill="#fff"/><rect x="12.3" y="11.5" width="3.4" height="10" fill="#fff"/></svg>
    <div class="abs download">DOWNLOAD NOW</div>

    <div class="abs pitch-title">How to make a perfect QOR PI project</div>
    <div class="abs pitch-btn btn-orange" style="top:194px">Get Nice Tools</div>
    <p class="abs pitch-text" style="left:733px;top:191px">Lorem ipsum dolor sit amet, consectetuer adipiscing elit. Nam nibh.</p>
    <div class="abs pitch-btn btn-green" style="top:258px">Get Right Ideas</div>
    <p class="abs pitch-text" style="left:739px;top:256px">Lorem ipsum dolor sit amet, consectetuer adipiscing elit. Nam nibh.</p>
    <div class="abs pitch-btn btn-blue" style="top:323px">Get It Done!</div>
    <p class="abs pitch-text" style="left:736px;top:320px">Lorem ipsum dolor sit amet, consectetuer adipiscing elit. Nam nibh.</p>
  </section>

  <main>
    <div class="abs panel" style="left:97px;top:486px;width:443px;height:267px"></div>
    <h3 class="abs panel-head head-green" style="left:106px;top:494px;width:428px;font-weight:400">Who We Are</h3>
    <div class="abs copy" style="left:113px;top:536px;width:196px">
      <p>Lorem ipsum dolor sit amet, consectetuer adipiscing elit. Nam nibh.</p><br>
      <p>Nunc varius facilisis eros. Sed erat. In in velit quis arcu ornare laoreet.</p><br>
      <p>Curabitur adipiscing luctus massa.Integer ut purus ac augue commodo commodo. Nunc nec mi eu justo tempor consectetuer. Etiam vitae nisl.</p>
    </div>
    <p class="abs copy" style="left:113px;top:721px">Lorem ipsum dolor sit amet, consectetuer&nbsp; adipiscing elit. Nam nibh.</p>
    <div class="abs photo" style="left:312px;top:535px;width:217px;height:152px" role="img" aria-label="Photo of a white modern low table"></div>

    <div class="abs panel" style="left:578px;top:486px;width:298px;height:267px"></div>
    <h3 class="abs panel-head head-orange" style="left:587px;top:494px;width:283px;font-weight:400">Support</h3>
    <span class="abs form-label" style="left:603px;top:555px">Your Name &nbsp;&nbsp;:</span>
    <span class="abs form-label" style="left:603px;top:588px">Your Email &nbsp;&nbsp;&nbsp;:</span>
    <span class="abs form-label" style="left:603px;top:621px">Your Quotation &nbsp;:</span>
    <div class="abs field" style="left:690px;top:549px;width:122px;height:24px"></div>
    <div class="abs field" style="left:690px;top:582px;width:122px;height:24px"></div>
    <div class="abs field" style="left:690px;top:614px;width:122px;height:73px"></div>
    <div class="abs submit-orange">Submit</div>

    <div class="abs panel" style="left:97px;top:791px;width:443px;height:266px"></div>
    <h3 class="abs panel-head head-blue" style="left:106px;top:799px;width:428px;font-weight:400">Recent Blog</h3>
    <div class="abs thumb photo" style="left:120px;top:846px;background:linear-gradient(135deg,#cfe0f0,#1c3358)" role="img" aria-label="Blog thumbnail of a bright sky scene"></div>
    <p class="abs date" style="left:206px;top:846px">25/12/2011</p>
    <p class="abs copy" style="left:206px;top:862px;width:200px">Lorem ipsum dolor sit amet, consectetuer adipiscing elit. Nam nibh.</p>
    <p class="abs more" style="left:205px;top:899px">read more &gt;&gt;</p>
    <div class="abs thumb photo" style="left:122px;top:919px;background:linear-gradient(135deg,#f2f2f2,#b8a090)" role="img" aria-label="Blog thumbnail portrait"></div>
    <p class="abs date" style="left:204px;top:928px">25/12/2011</p>
    <p class="abs copy" style="left:204px;top:944px">Lorem ipsum dolor sit amet, consectetuer&nbsp; adipiscing elit. Nam nibh.</p>
    <p class="abs more" style="left:205px;top:964px">read more &gt;&gt;</p>
    <div class="abs thumb photo" style="left:122px;top:990px;background:linear-gradient(135deg,#e8e8e8,#303030)" role="img" aria-label="Blog thumbnail of a person with an umbrella"></div>
    <p class="abs date" style="left:204px;top:996px">25/12/2011</p>
    <p class="abs copy" style="left:204px;top:1012px">Lorem ipsum dolor sit amet, consectetuer&nbsp; adipiscing elit. Nam nibh.</p>
    <p class="abs more" style="left:205px;top:1032px">read more &gt;&gt;</p>

    <div class="abs panel" style="left:578px;top:791px;width:298px;height:266px"></div>
    <h3 class="abs panel-head head-grey" style="left:587px;top:799px;width:283px;font-weight:400">Latest News</h3>
    <p class="abs date" style="left:591px;top:846px">25/12/2011</p>
    <p class="abs copy" style="left:591px;top:862px;width:135px">Lorem ipsum dolor sit amet, adipiscing elit. Nam nibh.</p>
    <p class="abs more" style="left:590px;top:899px">read more &gt;&gt;</p>
    <div class="abs photo" style="left:730px;top:837px;width:136px;height:99px;background:linear-gradient(135deg,#4f8fd8,#123a7a)" role="img" aria-label="News photo of a businessman before a stock chart"></div>
    <div class="abs newsletter"></div>
    <p class="abs newsletter-title">Subscribe on our monthly Newsletter:</p>
    <div class="abs field" style="left:631px;top:978px;width:171px;height:24px"></div>
    <div class="abs submit-dark">Submit</div>
  </main>

  <footer>
    <div class="abs footer"></div>
    <p class="abs foot-text" style="left:44px;top:1103px">42 Larchmere House 18 Ashgrove Road,<br>London SW9 4QT United Kingdom</p>
    <p class="abs foot-text" style="left:44px;top:1145px">Phone : +44(0)121 000 4817<br>Email : enquiries@velmoria.co.uk</p>
    <p class="abs foot-text" style="left:321px;top:1112px;word-spacing:2px">Disclaimer &nbsp;&nbsp;|&nbsp;&nbsp;&nbsp; Privacy Policy &nbsp;&nbsp;|&nbsp;&nbsp; Terms &amp; Conditions &nbsp;&nbsp;|&nbsp;&nbsp; Contact Us</p>
    <p class="abs foot-text" style="left:388px;top:1146px">Copyright 2011 Velmoria ,&nbsp; All Rights Reserved</p>
    <p class="abs foot-text" style="left:765px;top:1117px">Follow Us On :</p>
    <div class="abs social" style="left:850px"></div>
    <div class="abs social" style="left:880px;background:#45a7dc"></div>
    <div class="abs social" style="left:909px;background:#2f6ea8"></div>
    <p class="abs foot-text" style="left:780px;top:1153px">Subscribe &nbsp;:</p>
    <div class="abs feed"></div>
  </footer>

</div>
</body>
</html>
```